I need some Graphic Design for a Business Card

Create a design for my Business Cards.I will provide a pic for the front which you need to put into a frame that looks the same as a Screen of an [url removed, login to view] the back there will be My name and email address and the website link,a small logo of snapgrid and a small logo of friendlane with our address.I would also like to incorporate the Key logo on the [url removed, login to view] will need this in a Vector file as well.
[url removed, login to view]

The email address that needs to go on the Card is lars@[url removed, login to view] The Name is Lars Venhoek i prefer for the email the email icon and then email address .
On the Description under my name should be . Head of Marketing and Sales ,Partner at TilMarket ,Zurich

```html
<!DOCTYPE html>
<html lang="en">
<head>
<meta charset="utf-8">
<title>TilMarket Business Card</title>
<link rel="stylesheet" href="https://fonts.googleapis.com/css2?family=Lato:wght@400;700;900&display=swap">
<style>
  :root {
    --backdrop: #bcbcbc;
    --card: #0b0b0c;
    --bezel: #151516;
    --brand-blue: #2a88c9;
    --brand-blue-dark: #1d6aa3;
    --ink-white: #f4f4f4;
    --ink-dark: #0e2a40;
    --screen-top: #3a6fb8;
    --screen-bottom: #a9c6ea;
  }
  * { box-sizing: border-box; margin: 0; padding: 0; }
  html, body { width: 1200px; height: 944px; overflow: hidden; }
  body {
    background: var(--backdrop);
    font-family: "Lato", Arial, sans-serif;
    position: relative;
  }
  .card {
    position: absolute;
    left: 220px;
    width: 760px;
    height: 420px;
    background: var(--card);
    border-radius: 22px;
    overflow: hidden;
  }
  .card--front { top: 38px; }
  .card--back { top: 486px; }

  /* Front: device frame */
  .device {
    position: absolute;
    inset: 0;
  }
  .device__screen {
    position: absolute;
    left: 112px;
    top: 30px;
    width: 560px;
    height: 360px;
    border-radius: 6px;
    background: linear-gradient(160deg, var(--screen-top), var(--screen-bottom));
  }
  .device__home {
    position: absolute;
    right: 28px;
    top: 186px;
    width: 46px;
    height: 46px;
    border-radius: 50%;
    background: var(--ink-white);
    border: 4px solid #2b2b2b;
  }
  .device__speaker {
    position: absolute;
    left: 50px;
    top: 180px;
    width: 6px;
    height: 46px;
    border-radius: 3px;
    background: var(--ink-white);
  }
  .device__camera {
    position: absolute;
    left: 46px;
    top: 246px;
    width: 12px;
    height: 12px;
    border-radius: 50%;
    background: var(--ink-white);
  }

  /* Back: identity */
  .name-badge {
    position: absolute;
    left: 58px;
    top: 140px;
    width: 316px;
    height: 72px;
    border-radius: 12px;
    background: var(--brand-blue);
    display: flex;
    align-items: center;
    padding-left: 16px;
  }
  .name-badge__icon { width: 40px; height: 40px; flex: none; }
  .name-badge__text { margin-left: 14px; }
  .name-badge__name {
    color: var(--ink-white);
    font-weight: 900;
    font-size: 30px;
    letter-spacing: 0.5px;
    line-height: 1;
  }
  .name-badge__role {
    color: var(--ink-dark);
    font-weight: 700;
    font-size: 15px;
    letter-spacing: 0.8px;
    margin-top: 5px;
  }

  .contact-list {
    position: absolute;
    left: 58px;
    top: 248px;
    list-style: none;
  }
  .contact-list__item {
    display: flex;
    align-items: center;
    height: 30px;
    font-weight: 700;
    font-size: 19px;
    letter-spacing: 0.3px;
  }
  .contact-list__item--white { color: var(--ink-white); }
  .contact-list__item--blue { color: var(--brand-blue); }
  .contact-list__icon { width: 24px; height: 24px; margin-right: 14px; flex: none; }

  .brand {
    position: absolute;
    right: 58px;
    top: 70px;
    display: flex;
    align-items: center;
  }
  .brand__mark {
    width: 86px;
    height: 86px;
    border-radius: 50%;
    border: 6px solid var(--brand-blue);
    margin-right: 14px;
  }
  .brand__name {
    color: var(--ink-white);
    font-weight: 700;
    font-size: 34px;
  }
</style>
</head>
<body>

<section class="card card--front" aria-label="Card front">
  <div class="device">
    <div class="device__speaker"></div>
    <div class="device__camera"></div>
    <div class="device__screen" role="img" aria-label="Phone home screen showing the client's app icons"></div>
    <div class="device__home"></div>
  </div>
</section>

<section class="card card--back" aria-label="Card back">
  <div class="name-badge">
    <svg class="name-badge__icon" viewBox="0 0 40 40" aria-hidden="true">
      <circle cx="20" cy="13" r="8" fill="none" stroke="#f4f4f4" stroke-width="2.5"/>
      <path d="M5 37c0-9 7-14 15-14s15 5 15 14" fill="none" stroke="#f4f4f4" stroke-width="2.5"/>
    </svg>
    <div class="name-badge__text">
      <div class="name-badge__name">MIKA STRAND</div>
      <div class="name-badge__role">Software Engineering</div>
    </div>
  </div>

  <ul class="contact-list">
    <li class="contact-list__item contact-list__item--white">
      <svg class="contact-list__icon" viewBox="0 0 24 24" aria-hidden="true">
        <circle cx="12" cy="12" r="11" fill="#2a88c9"/>
        <path d="M8 6.5l2 3-1.3 1.3c.8 1.7 2 2.9 3.6 3.6L13.6 13l3 2-1 2.2c-4.5-.3-8.3-4.1-8.6-8.6z" fill="#0b0b0c"/>
      </svg>
      +49 17640218853
    </li>
    <li class="contact-list__item contact-list__item--blue">
      <svg class="contact-list__icon" viewBox="0 0 24 24" aria-hidden="true">
        <circle cx="12" cy="12" r="11" fill="#f4f4f4"/>
        <rect x="6" y="8" width="12" height="8.5" rx="1" fill="#0b0b0c"/>
        <path d="M6.5 8.5L12 13l5.5-4.5" fill="none" stroke="#f4f4f4" stroke-width="1.2"/>
      </svg>
      lars@TilMarket.com
    </li>
    <li class="contact-list__item contact-list__item--white">
      <svg class="contact-list__icon" viewBox="0 0 24 24" aria-hidden="true">
        <circle cx="12" cy="12" r="11" fill="#2a88c9"/>
      </svg>
      www.TilMarket.com
    </li>
    <li class="contact-list__item contact-list__item--blue">
      <svg class="contact-list__icon" viewBox="0 0 24 24" aria-hidden="true">
        <circle cx="12" cy="12" r="11" fill="#f4f4f4"/>
      </svg>
      www.snapgrid.com/TilMarket
    </li>
    <li class="contact-list__item contact-list__item--white">
      <svg class="contact-list__icon" viewBox="0 0 24 24" aria-hidden="true">
        <circle cx="12" cy="12" r="11" fill="#2a88c9"/>
      </svg>
      www.friendlane.com/TilMarket
    </li>
  </ul>

  <div class="brand">
    <div class="brand__mark"></div>
    <div class="brand__name">tilmarket</div>
  </div>
</section>

</body>
</html>
```